Powerpoint Template needed for new Digital Consultancy

We have recently had our logo designed through Sketchmarket and would now like to extend the brand look & feel through to having a powerpoint template created that we can use as a master template within which to create our client presentations.
Typical slides required and in terms of what we would need templating is:

- Stylised header and footer for main content slides
- intro/front page slide
- contents page slide
- standardised font type and sizes, heading types (including sizes) for Level 1, Level 2 and Level 3 headings
- use of text colour and any standards/styling around when to use bold, underline, italics etc
- table styling for when we want to use tables in the presentation
- standards and styles around using bullet and number lists
- stylising use of imagery that is dropped in e.g. do all images have a certain border style or drop-shadow etc.
- style and slide layout/format for how team profiles are handled
- style and slide layout/format for how case studies are handled
- closing, contact-us page

We can send over logo files and colour/font styles etc used for the logo soon.

Target Market(s)

B2B professional clients that are either medium to large corporations or potentially some government departments.

Industry/Entity Type

Digital

Font styles to use
Sans Serif

Colors
ec1f27
f37122
f78f20
faa54b
f68d4d
0255a3

Requirements
Must have
• Ideally as many templated pages/master slide types as outlined above in the brief to meet the requirements of what the powerpoint deck will be used for. Namely client presentations and pitches.
• Versions of the logo are attached to give an idea of the colour palette and clean, modern style we are looking for, plus the type of font we are using and like.
• We are looking for the slide design to be modern, minimalistic, clean and not overuse of colour. Preferably a white slide background so it's easy to then read slide content when we populate the slides with text which will be in black.
Nice to have
• Not expecting to see too much more than simple use of the logo and a slide header perhaps using some sort of line as a break and then a simple footer as well.
• Consider using Abode font.
Should not have
• Too much block colour or elements that draw away from what will go in the main content body of our slides when we use them.

```html
<!DOCTYPE html>
<html lang="en">
<head>
<meta charset="utf-8">
<title>Brightloop Slide Template Overview</title>
<link href="https://fonts.googleapis.com/css2?family=Roboto:wght@300;400;500;700&display=swap" rel="stylesheet">
<style>
  :root {
    --canvas: #cbcbcb;
    --paper: #ffffff;
    --red: #ec1f27;
    --orange: #f37122;
    --amber: #f78f20;
    --ink: #1f1f1f;
    --charcoal: #2b2b2b;
    --slate: #4d4d4d;
    --grey: #8c8c8c;
    --grey-light: #a9a9a9;
    --grey-pale: #d9d9d9;
    --muted: #9a9a9a;
  }
  * { box-sizing: border-box; margin: 0; padding: 0; }
  html, body { width: 1200px; height: 1200px; overflow: hidden; }
  body { background: var(--canvas); font-family: "Roboto", Arial, sans-serif; color: var(--ink); position: relative; }

  .slide { position: absolute; background: var(--paper); overflow: hidden; }
  .slide > * { position: absolute; }
  .section-label { font-size: 3.5px; letter-spacing: .8px; color: #c9c9c9; text-transform: uppercase; line-height: 1; }
  .slide-title { font-size: 9.5px; font-weight: 500; letter-spacing: .6px; color: var(--ink); white-space: nowrap; line-height: 1; }
  .title-rule { width: 22px; height: 1.6px; background: var(--red); }
  .brand { font-size: 7px; font-weight: 500; color: var(--ink); line-height: 1; white-space: nowrap; }
  .footer-url { font-size: 3.5px; color: var(--muted); }
  .page-num { width: 10px; height: 10px; border: .6px solid #bbb; border-radius: 50%; font-size: 3px; color: #999; display: flex; align-items: center; justify-content: center; }
  .tiny { font-size: 3.6px; line-height: 1.45; color: #777; }
  .label-strong { font-size: 4.4px; font-weight: 700; color: var(--ink); }
  .icon-dot { border-radius: 50%; display: flex; align-items: center; justify-content: center; flex: none; }
  svg { display: block; }

  .slide--bars { left: 67px; top: 29px; width: 426px; height: 239px; }
  .slide--area { left: 551px; top: 29px; width: 442px; height: 249px; }
  .slide--map { left: 67px; top: 306px; width: 434px; height: 244px; }
  .slide--tiles { left: 551px; top: 306px; width: 444px; height: 250px; }
  .slide--contact { left: 67px; top: 602px; width: 440px; height: 248px; }

  .stat-item { display: flex; gap: 3px; align-items: flex-start; }
  .stat-item .text { width: 50px; }

  .legend-item { display: flex; gap: 8px; align-items: flex-start; }
  .legend-item .name { font-size: 4.6px; color: var(--ink); margin-bottom: 1px; }
  .legend-item .name.is-accent { color: var(--red); }
  .legend-item .tiny { width: 72px; }

  .value-pill { background: var(--amber); color: #fff; font-size: 13px; font-weight: 400; border-radius: 13px; display: flex; align-items: center; justify-content: center; }
  .user-stat { display: flex; gap: 3px; align-items: center; }
  .user-stat .value { font-size: 8px; font-weight: 700; color: var(--red); }
  .user-stat .caption { font-size: 3.4px; color: #777; }

  .service-item { display: flex; gap: 7px; align-items: flex-start; }
  .service-item .name { font-size: 5px; color: var(--ink); margin-bottom: 1.5px; }
  .service-item .name.is-accent { color: var(--red); }
  .service-item .name.is-muted { color: #888; }
  .service-item .tiny { width: 110px; }

  .tile-quote { background: var(--amber); display: flex; align-items: center; justify-content: center; }
  .tile-list { background: var(--charcoal); border: 1px solid #111; padding: 10px 6px 0 10px; }
  .tile-list li { list-style: none; font-size: 3.6px; color: #eee; line-height: 1.9; padding-left: 6px; position: relative; }
  .tile-list li.tick::before { content: "\2713"; position: absolute; left: 0; font-size: 3.6px; }
  .tile-list li + li.tick { margin-top: 3px; }

  .contact-row { display: flex; align-items: center; gap: 8px; }
  .contact-main { font-size: 8.5px; color: var(--ink); }
  .contact-sub { font-size: 4.6px; font-weight: 500; color: var(--ink); margin-top: 3px; }
</style>
</head>
<body>

<section class="slide slide--bars">
  <div class="section-label" style="left:22px;top:17px;">Section One</div>
  <h2 class="slide-title" style="left:22px;top:25px;">Creative Visual Design</h2>
  <div class="title-rule" style="left:22px;top:40px;"></div>
  <div class="brand" style="left:370px;top:13px;">Brightloop</div>

  <svg style="left:0;top:0;" width="426" height="239" viewBox="0 0 426 239">
    <g stroke="#bbb" stroke-width=".5">
      <line x1="42" y1="64" x2="42" y2="140"/><line x1="115" y1="64" x2="115" y2="140"/>
      <line x1="189" y1="64" x2="189" y2="140"/><line x1="262" y1="64" x2="262" y2="140"/>
      <line x1="336" y1="64" x2="336" y2="140"/>
    </g>
    <g>
      <rect x="46" y="125" width="11" height="14" fill="#a9a9a9"/><rect x="57" y="117" width="11" height="22" fill="#5a5a5a"/><rect x="68" y="110" width="11" height="29" fill="#222"/><rect x="79" y="96" width="11" height="43" fill="#ec1f27"/>
      <rect x="119" y="135" width="11" height="4" fill="#a9a9a9"/><rect x="130" y="122" width="11" height="17" fill="#5a5a5a"/><rect x="141" y="125" width="11" height="14" fill="#222"/><rect x="152" y="116" width="11" height="23" fill="#ec1f27"/>
      <rect x="193" y="67" width="11" height="72" fill="#a9a9a9"/><rect x="204" y="101" width="11" height="38" fill="#5a5a5a"/><rect x="215" y="88" width="11" height="51" fill="#222"/><rect x="226" y="113" width="11" height="26" fill="#ec1f27"/>
      <rect x="266" y="122" width="11" height="17" fill="#a9a9a9"/><rect x="277" y="106" width="11" height="33" fill="#5a5a5a"/><rect x="288" y="81" width="11" height="58" fill="#222"/><rect x="299" y="131" width="11" height="8" fill="#f37122"/>
      <rect x="340" y="98" width="11" height="41" fill="#a9a9a9"/><rect x="351" y="131" width="11" height="8" fill="#5a5a5a"/><rect x="362" y="125" width="11" height="14" fill="#222"/><rect x="373" y="127" width="11" height="12" fill="#ec1f27"/>
    </g>
    <g font-size="3" fill="#bbb" font-family="Roboto, sans-serif">
      <text x="64" y="146">2010</text><text x="137" y="146">2011</text><text x="211" y="146">2012</text><text x="284" y="146">2013</text><text x="358" y="146">2014</text>
    </g>
  </svg>

  <div class="stat-item" style="left:49px;top:172px;">
    <div class="icon-dot" style="width:19px;height:19px;background:#9a9a9a;"><svg width="8" height="5" viewBox="0 0 8 5"><rect x=".5" y=".5" width="7" height="4" rx="2" fill="none" stroke="#fff" stroke-width=".8"/></svg></div>
    <div class="text"><div class="label-strong">Number One</div><div class="tiny">Lemon drops oat cake cake sugar plum sweet tart.</div></div>
  </div>
  <div class="stat-item" style="left:136px;top:172px;">
    <div class="icon-dot" style="width:19px;height:19px;background:#4d4d4d;"><svg width="7" height="7" viewBox="0 0 7 7"><path d="M6.5.5 1 3l2.5 1 1 2.5z" fill="#fff"/></svg></div>
    <div class="text"><div class="label-strong">Number Two</div><div class="tiny">Lemon drops oat cake cake sugar plum sweet tart.</div></div>
  </div>
  <div class="stat-item" style="left:222px;top:172px;">
    <div class="icon-dot" style="width:19px;height:19px;background:#1f1f1f;"><svg width="8" height="8" viewBox="0 0 8 8"><circle cx="4" cy="4" r="3" fill="none" stroke="#fff" stroke-width=".9"/><circle cx="4" cy="4" r="1.1" fill="#fff"/></svg></div>
    <div class="text"><div class="label-strong">Number Three</div><div class="tiny">Lemon drops oat cake cake sugar plum sweet tart.</div></div>
  </div>
  <div class="stat-item" style="left:309px;top:172px;">
    <div class="icon-dot" style="width:19px;height:19px;background:#ec1f27;"><svg width="6" height="7" viewBox="0 0 6 7"><path d="M.5 .8h5v2.6c0 1.8-1.2 2.8-2.5 3.3C1.7 6.2.5 5.2.5 3.4z" fill="#fff"/></svg></div>
    <div class="text"><div class="label-strong">Number Four</div><div class="tiny">Lemon drops oat cake cake sugar plum sweet tart.</div></div>
  </div>

  <div class="footer-url" style="left:13px;top:224px;">www. brightloop.com</div>
  <div class="page-num" style="left:404px;top:222px;">34</div>
</section>

<section class="slide slide--area">
  <div class="section-label" style="left:23px;top:17px;">Section One</div>
  <h2 class="slide-title" style="left:23px;top:26px;">Creative Visual Design</h2>
  <div class="title-rule" style="left:23px;top:41px;"></div>
  <div class="brand" style="left:388px;top:14px;">Brightloop</div>

  <svg style="left:0;top:0;" width="270" height="210" viewBox="0 0 270 210">
    <line x1="77" y1="77" x2="77" y2="189" stroke="#bbb" stroke-width=".5"/>
    <line x1="77" y1="189" x2="246" y2="189" stroke="#bbb" stroke-width=".5"/>
    <path d="M77 145 118 93 159 109 201 99 245 103V189H77Z" fill="#a3a3a3"/>
    <path d="M77 145H118L159 130 201 119 245 123V189H77Z" fill="#555"/>
    <path d="M77 169 118 163 159 123 201 159 245 149V189H77Z" fill="#232323"/>
    <path d="M77 182H118L159 175 201 138 245 181V189H77Z" fill="#f78f20"/>
    <g font-size="3" fill="#aaa" font-family="Roboto, sans-serif" text-anchor="end">
      <text x="74" y="80">30</text><text x="74" y="99">25</text><text x="74" y="118">20</text><text x="74" y="136">15</text><text x="74" y="155">10</text><text x="74" y="174">5</text><text x="74" y="190">0</text>
    </g>
    <g font-size="3" fill="#aaa" font-family="Roboto, sans-serif" text-anchor="middle">
      <text x="77" y="196">2010</text><text x="118" y="196">2011</text><text x="159" y="196">2012</text><text x="201" y="196">2013</text><text x="245" y="196">2014</text>
    </g>
  </svg>

  <div class="legend-item" style="left:272px;top:77px;">
    <div class="icon-dot" style="width:22px;height:22px;background:var(--amber);"><svg width="9" height="9" viewBox="0 0 9 9"><circle cx="4.5" cy="4.5" r="3.5" fill="none" stroke="#fff"/><circle cx="4.5" cy="4.5" r="1.3" fill="#fff"/></svg></div>
    <div><div class="name is-accent">Type A</div><div class="tiny">Lemon drops oat cake oat cake sugar plum sweet. Chocolate cake sweet pastry.</div></div>
  </div>
  <div class="legend-item" style="left:272px;top:108px;">
    <div class="icon-dot" style="width:22px;height:22px;background:#1f1f1f;"><svg width="7" height="8" viewBox="0 0 7 8"><path d="M.5.5h4l2 2v5H.5z" fill="#fff"/></svg></div>
    <div><div class="name">Type B</div><div class="tiny">Lemon drops oat cake oat cake sugar plum sweet. Chocolate cake sweet pastry.</div></div>
  </div>
  <div class="legend-item" style="left:272px;top:140px;">
    <div class="icon-dot" style="width:22px;height:22px;background:#4d4d4d;"><svg width="8" height="8" viewBox="0 0 7 7"><path d="M6.5.5 1 3l2.5 1 1 2.5z" fill="#fff"/></svg></div>
    <div><div class="name">Type C</div><div class="tiny">Lemon drops oat cake oat cake sugar plum sweet. Chocolate cake sweet pastry.</div></div>
  </div>
  <div class="legend-item" style="left:272px;top:171px;">
    <div class="icon-dot" style="width:22px;height:22px;background:#9a9a9a;"><svg width="9" height="5" viewBox="0 0 8 5"><rect x=".5" y=".5" width="7" height="4" rx="2" fill="none" stroke="#fff" stroke-width=".8"/></svg></div>
    <div><div class="name" style="color:#777;">Type D</div><div class="tiny">Lemon drops oat cake oat cake sugar plum sweet. Chocolate cake sweet pastry.</div></div>
  </div>

  <div class="footer-url" style="left:13px;top:233px;">www. brightloop.com</div>
  <div class="page-num" style="left:419px;top:231px;">35</div>
</section>

<section class="slide slide--map">
  <div class="section-label" style="left:22px;top:17px;">Section One</div>
  <h2 class="slide-title" style="left:22px;top:26px;">Creative Visual Design</h2>
  <div class="title-rule" style="left:22px;top:41px;"></div>
  <div class="brand" style="left:383px;top:11px;">Brightloop</div>

  <div role="img" aria-label="Grey map of North America" style="left:50px;top:55px;width:143px;height:126px;border-radius:40% 55% 45% 35%;background:radial-gradient(ellipse at 55% 45%, #b8b8b8 0%, #c8c8c8 60%, rgba(255,255,255,0) 72%);"></div>
  <div class="value-pill" style="left:89px;top:108px;width:66px;height:26px;">359 M</div>

  <div class="user-stat" style="left:61px;top:190px;">
    <div class="icon-dot" style="width:18px;height:18px;background:var(--amber);"><svg width="5" height="9" viewBox="0 0 5 9"><circle cx="2.5" cy="1.3" r="1.2" fill="#fff"/><rect x="1" y="3" width="3" height="5.5" rx=".8" fill="#fff"/></svg></div>
    <div><div class="value">1.908 K</div><div class="caption">Male User</div></div>
  </div>
  <div class="user-stat" style="left:125px;top:190px;">
    <div class="icon-dot" style="width:18px;height:18px;background:var(--amber);"><svg width="6" height="9" viewBox="0 0 6 9"><circle cx="3" cy="1.3" r="1.2" fill="#fff"/><path d="M3 2.8 5.5 6.5H.5z" fill="#fff"/><rect x="2" y="6" width="2" height="2.6" fill="#fff"/></svg></div>
    <div><div class="value">2.074 K</div><div class="caption">Female User</div></div>
  </div>

  <div class="label-strong" style="left:223px;top:54px;font-size:5px;font-weight:500;">Data Analysis</div>
  <p class="tiny" style="left:223px;top:65px;width:155px;">Liquorice chupa chups applicake apple pie cupcake brownie bear claw jelly pie tart gingerbread cotton candy. Bear claw croissant apple pie. Croissant cake tart pastry liquorice tart pastry biscuit wafer sweet apple pie.</p>

  <svg style="left:215px;top:94px;" width="170" height="80" viewBox="0 0 170 80">
    <g stroke="#e6e6e6" stroke-width=".4">
      <line x1="14" y1="4" x2="165" y2="4"/><line x1="14" y1="16" x2="165" y2="16"/><line x1="14" y1="28" x2="165" y2="28"/>
      <line x1="14" y1="41" x2="165" y2="41"/><line x1="14" y1="53" x2="165" y2="53"/><line x1="14" y1="66" x2="165" y2="66"/>
    </g>
    <g font-size="4" fill="#888" font-family="Roboto, sans-serif" text-anchor="end">
      <text x="9" y="6">5</text><text x="9" y="18">4</text><text x="9" y="30">3</text><text x="9" y="43">2</text><text x="9" y="55">1</text><text x="9" y="68">0</text>
    </g>
    <rect x="28" y="24" width="14" height="42" fill="#a9a9a9"/>
    <rect x="56" y="36" width="14" height="30" fill="#8c8c8c"/>
    <rect x="84" y="24" width="14" height="42" fill="#4d4d4d"/>
    <rect x="113" y="12" width="14" height="54" fill="#1f1f1f"/>
    <rect x="141" y="22" width="14" height="44" fill="#ec1f27"/>
    <g font-size="4.5" fill="#777" font-family="Roboto, sans-serif" text-anchor="middle">
      <text x="35" y="77">2010</text><text x="63" y="77">2011</text><text x="91" y="77">2012</text><text x="120" y="77">2013</text><text x="148" y="77">2014</text>
    </g>
  </svg>

  <div style="left:225px;top:180px;width:1.5px;height:21px;background:#ccc;"></div>
  <p class="tiny" style="left:233px;top:180px;width:155px;">Liquorice chupa chups applicake apple pie cupcake brownie bear claw cake gingerbread cotton candy. Bear claw croissant apple pie. Croissant cake sweet puff oreo. Liquorice chupa chups applicake apple pie.</p>

  <div class="footer-url" style="left:13px;top:228px;">www. brightloop.com</div>
  <div class="page-num" style="left:415px;top:225px;">36</div>
</section>

<section class="slide slide--tiles">
  <div class="section-label" style="left:23px;top:17px;">Section Five</div>
  <h2 class="slide-title" style="left:23px;top:26px;">Creative Tile With Image</h2>
  <div class="title-rule" style="left:23px;top:41px;"></div>
  <div class="brand" style="left:390px;top:12px;">Brightloop</div>

  <div class="label-strong" style="left:49px;top:57px;font-weight:500;">Company Data Analysis</div>
  <p class="tiny" style="left:49px;top:67px;width:150px;">Liquorice chupa chups sweet pie applicake apple pie cupcake brownie bear claw cake pie gingerbread cotton candy. Caramels icing lemon drops dessert sugar plum macaroon. Macaroon caramels sweet roll jujubes soufflé.</p>

  <div class="service-item" style="left:48px;top:100px;">
    <div class="icon-dot" style="width:22px;height:22px;background:var(--amber);"><svg width="9" height="7" viewBox="0 0 9 7"><rect x=".5" y=".5" width="8" height="4.5" fill="none" stroke="#fff" stroke-width=".8"/><path d="M3 6.5h3" stroke="#fff" stroke-width=".8"/></svg></div>
    <div><div class="name is-accent">Business Strategy</div><div class="tiny">Caramels icing lemon drops dessert sugar plum macaroon. Macaroon caramels sweet roll jujubes soufflé.</div></div>
  </div>
  <div class="service-item" style="left:48px;top:131px;">
    <div class="icon-dot" style="width:22px;height:22px;background:#1f1f1f;"><svg width="8" height="8" viewBox="0 0 8 8"><circle cx="4" cy="1.5" r="1" fill="none" stroke="#fff" stroke-width=".7"/><path d="M4 2.5v5M1 5c.5 2 5.5 2 6 0M2.5 3.8h3" fill="none" stroke="#fff" stroke-width=".7"/></svg></div>
    <div><div class="name">Creative Solution</div><div class="tiny">Caramels icing lemon drops dessert sugar plum macaroon. Macaroon caramels sweet roll jujubes soufflé.</div></div>
  </div>
  <div class="service-item" style="left:48px;top:163px;">
    <div class="icon-dot" style="width:22px;height:22px;background:#4d4d4d;"><svg width="6" height="7" viewBox="0 0 6 7"><path d="M.5 .8h5v2.6c0 1.8-1.2 2.8-2.5 3.3C1.7 6.2.5 5.2.5 3.4z" fill="#fff"/></svg></div>
    <div><div class="name">File Manager</div><div class="tiny">Caramels icing lemon drops dessert sugar plum macaroon. Macaroon caramels sweet roll jujubes soufflé.</div></div>
  </div>
  <div class="service-item" style="left:48px;top:194px;">
    <div class="icon-dot" style="width:22px;height:22px;background:#9a9a9a;"><svg width="8" height="6" viewBox="0 0 8 6"><path d="M.5 .5h3v3l-1.5 2H.8l1.2-2H.5zM4.5 .5h3v3l-1.5 2H4.8L6 3.5H4.5z" fill="#fff"/></svg></div>
    <div><div class="name is-muted">Desktop Application</div><div class="tiny">Caramels icing lemon drops dessert sugar plum macaroon. Macaroon caramels sweet roll jujubes soufflé.</div></div>
  </div>

  <div role="img" aria-label="Placeholder for a featured photograph" style="left:221px;top:58px;width:79px;height:159px;background:#d9d9d9;"></div>
  <div class="tile-quote" style="left:303px;top:58px;width:79px;height:78px;">
    <svg width="36" height="30" viewBox="0 0 36 30"><path d="M2 2h14v14l-6 12H3l5-12H2zM20 2h14v14l-6 12h-7l5-12h-6z" fill="#fff"/></svg>
  </div>
  <ul class="tile-list" style="left:303px;top:139px;width:79px;height:78px;">
    <li class="tick">Lemon drops oat cake oat</li>
    <li>cake sugar plum sweet</li>
    <li class="tick">Chocolate cake sweet</li>
    <li>pastry candy canes</li>
    <li>chocolate cake sesame</li>
    <li class="tick">Oreo cake lollipop sweet</li>
  </ul>

  <div class="page-num" style="left:421px;top:235px;">37</div>
</section>

<section class="slide slide--contact">
  <div role="img" aria-label="Brand stationery scene for Solenne with business cards, a key tag, a tablet and an office address card for Unit 4 Harbour Row, Eastfield 20417" style="left:0;top:0;width:440px;height:174px;background:linear-gradient(180deg,#e4e4e4 0%,#efefef 55%,#d6d6d6 100%);"></div>
  <div style="left:0;top:174px;width:440px;height:74px;background:var(--paper);"></div>

  <div style="left:46px;top:203px;font-size:12px;color:#333;font-weight:400;">Get In Touch</div>

  <div class="contact-row" style="left:174px;top:198px;">
    <div class="icon-dot" style="width:24px;height:24px;background:var(--amber);"><svg width="12" height="9" viewBox="0 0 12 9"><rect x=".6" y=".6" width="10.8" height="7.8" fill="none" stroke="#fff"/><path d="M.6.6 6 5l5.4-4.4" fill="none" stroke="#fff"/></svg></div>
    <div><div class="contact-main">hello@fernway.com</div><div class="contact-sub">We are here to help you</div></div>
  </div>
  <div class="contact-row" style="left:290px;top:198px;">
    <div class="icon-dot" style="width:24px;height:24px;background:var(--amber);"><svg width="11" height="11" viewBox="0 0 11 11"><path d="M2.2.8 4 3 3 4.4c.8 1.6 2 2.8 3.6 3.6L8 7l2.2 1.8-1 1.6C5 10 1 6 .6 1.8z" fill="#fff"/></svg></div>
    <div><div class="contact-main">01 2760 3184</div><div class="contact-sub">Working days 9am to 7pm</div></div>
  </div>
</section>

</body>
</html>
```